Marketing Web Site Design for a Mobile CRM Sales Rep App

We are Vetrasol. We need a web site design to help sell our customizable mobile CRM B2B sales rep app. The site will be used as a sales tool and for lead capture. Our main competitors are brindolo.com and tarnwickhub.com. The site will be about 6 to 10 pages. Take a look at brindolo.com for an example of the type of content that will be on our site.

Target Market(s)

Manufacturers and distributors who have an outside sales force that service retail stores.

Contact Information for Business Card

Malcolm Ashdown
President
3176 Fern Hollow Rd #512
Sarasota, Florida 34233

o: 941.555.0147
m: 941.555.0193

e: mashdown@vetrasol.example

Routes made Simple

Number of Pages Required

5+ page

Requirements
Must have
• We like how the content on the brindolo.com site is organized. We are not asking that you copy it. Use it for ideas. Here are some pages we need.
• 1. Need a Home Page like: https://www.brindolo.com
• 2. Need an Integration Page like: https://www.brindolo.com/plugin-directory/
• 3. Need a Lead Capture Page like: https://www.brindolo.com/request-a-demo-2/?utm_expid=71942036-13.qzmevyRfA4LLWHT8pbnkTR.0&utm_referrer=https%3A%2F%2Fwww.brindolo.com%2Fplugin-directory%2F
• 4. Need a Contact Us Page like: https://www.brindolo.com/contact/
• 5. Need a Feature Page like: https://www.brindolo.com/platform-overview/

```html
<!DOCTYPE html>
<html lang="en">
<head>
<meta charset="utf-8">
<title>Vetrasol — Mobile CRM for Sales Reps</title>
<link href="https://fonts.googleapis.com/css2?family=Poppins:wght@600;700&family=Open+Sans:wght@400;600;700&display=swap" rel="stylesheet">
<style>
:root{
  --sky:#37c6f2;
  --sky-soft:#e6f7fd;
  --ink:#111;
  --body:#333;
  --navy:#0b3f6e;
  --dark:#2b2b2b;
  --footer:#1c1a19;
  --gold:#f5b921;
  --line:#e3e3e3;
}
*{box-sizing:border-box;margin:0;padding:0}
html,body{width:1200px;height:3674px;overflow:hidden}
body{font-family:"Open Sans",sans-serif;color:var(--body);background:#fff;font-size:14px}
h1,h2,.brand{font-family:"Poppins",sans-serif}
.wrap{width:1000px;margin:0 auto;position:relative}

.topbar{height:63px;background:var(--sky);color:#fff;font-size:14px}
.topbar .wrap{display:flex;align-items:center;height:63px;justify-content:space-between}
.topbar .contact{display:flex;align-items:center;gap:8px}
.topbar .actions{display:flex;align-items:center;gap:26px}
.btn-white{background:#fff;color:var(--ink);padding:9px 17px;border-radius:3px;font-size:14px}

.nav{height:74px;background:#fff;border-bottom:1px solid #eee}
.nav .wrap{display:flex;align-items:center;justify-content:space-between;height:74px}
.brand{font-size:38px;font-weight:600;color:var(--ink);display:flex;align-items:center;gap:10px;letter-spacing:-1px}
.brand .dot{width:14px;height:14px;background:var(--sky)}
.menu{display:flex;gap:34px;font-size:14px;color:var(--ink)}
.menu .on{color:var(--sky);font-weight:600}

.hero{height:402px;background:linear-gradient(100deg,#0a2f5a 0%,#0e4f86 45%,#1d7fc0 75%,#0b3462 100%);position:relative;color:#fff}
.hero .art{position:absolute;right:0;top:0;width:470px;height:402px;background:radial-gradient(circle at 55% 45%,#41c0e8 0%,#1a6fae 45%,rgba(11,52,98,0) 75%)}
.hero h1{position:absolute;left:97px;top:47px;font-size:56px;line-height:70px;font-weight:700}
.hero h1 span{color:var(--sky)}
.hero p{position:absolute;left:99px;top:215px;width:445px;font-size:13px;line-height:19px}
.btn-sky{display:inline-block;background:var(--sky);color:#fff;font-size:14px;padding:12px 21px;border-radius:3px}
.hero .btn-sky{position:absolute;left:99px;top:305px}

.intro{height:267px;background:var(--sky-soft);text-align:center;padding-top:60px}
.intro h2{font-size:36px;color:var(--ink)}
.intro p{width:950px;margin:28px auto 0;font-size:14px;line-height:22px;color:var(--ink)}

.section{text-align:center}
.section h2{font-size:36px;color:var(--ink);font-weight:700}
.section .lead{font-size:14px;color:var(--ink);margin-top:18px}
.cards{display:flex;justify-content:space-between;width:1000px;margin:0 auto}

.features{height:628px;padding-top:75px}
.features .cards{margin-top:70px}
.feature{width:230px;height:314px;border:1px solid var(--line);padding-top:28px}
.feature .icon{width:115px;height:115px;margin:0 auto;border-radius:50%}
.feature h3{font-size:18px;color:var(--ink);margin-top:30px;font-weight:600}
.feature p{font-size:14px;line-height:22px;margin:10px auto 0;width:190px}

.cta{height:320px;background:linear-gradient(90deg,#3a3a3a,#2a2a2a 50%,#3c3834);text-align:center;color:#fff;padding-top:60px}
.cta h2{font-size:38px;font-weight:700}
.cta p{width:660px;margin:22px auto 0;font-size:14px;line-height:22px}
.cta .btn-sky{margin-top:30px;width:146px;text-align:center}

.gallery{height:612px;padding-top:72px}
.gallery .cards{margin-top:75px}
.tile{width:230px;height:297px;position:relative;color:#fff;overflow:hidden}
.tile .cap{position:absolute;left:0;right:0;top:0;height:36px;background:rgba(30,30,30,.7);font-weight:700;font-size:17px;line-height:36px}
.tile .plus{position:absolute;right:0;bottom:0;width:62px;height:62px;background:var(--sky);font-size:24px;line-height:62px}
.tile .over{position:absolute;inset:0;background:rgba(40,40,40,.78);padding-top:100px}
.tile .over h3{font-size:17px;font-weight:700}
.tile .over p{font-size:13px;line-height:16px;width:180px;margin:22px auto 0}
.tile .over .more{color:var(--gold);font-size:13px;margin-top:16px}

.offers{height:613px;padding-top:72px}
.offers .cards{margin-top:75px}
.offer{width:230px;height:297px;position:relative;color:#fff}
.offer h3{position:absolute;top:137px;left:0;right:0;font-size:17px;font-weight:700}
.offer .more{position:absolute;top:247px;left:0;right:0;font-size:13px}

.footer{height:314px;background:var(--footer);color:#fff}
.footer .wrap{display:flex;padding-top:68px}
.footer .brand{color:#fff;font-size:36px;margin-top:48px;width:286px}
.footer h4{font-size:16px;font-weight:700;margin-bottom:6px}
.footer p,.footer li{font-size:13px;line-height:24px;list-style:none}
.footer .addr{width:338px}
.footer .links{width:222px}
.footer .links .on{color:var(--sky);font-weight:700}
.social{display:flex;gap:10px;margin-top:20px}
.social span{width:25px;height:25px;border-radius:50%;background:#fff}
.copy{height:61px;background:var(--sky);color:#fff;font-size:10px;text-align:center;line-height:61px}
</style>
</head>
<body>

<header class="topbar">
  <div class="wrap">
    <div class="contact">
      <svg width="18" height="18" viewBox="0 0 24 24" fill="none" stroke="#fff" stroke-width="2"><path d="M5 3h4l2 5-3 2a11 11 0 0 0 6 6l2-3 5 2v4a2 2 0 0 1-2 2A17 17 0 0 1 3 5a2 2 0 0 1 2-2z"/></svg>
      <span>+000+000+000 |</span>
      <svg width="18" height="14" viewBox="0 0 24 18" fill="none" stroke="#fff" stroke-width="2"><rect x="1" y="1" width="22" height="16"/><path d="M1 1l11 9 11-9"/></svg>
      <span>info@example.com</span>
    </div>
    <div class="actions">
      <span>
        <svg width="16" height="16" viewBox="0 0 24 24" fill="#fff" style="vertical-align:-3px"><circle cx="12" cy="7" r="5"/><path d="M2 23c0-6 4-9 10-9s10 3 10 9z"/></svg>
        Login
      </span>
      <span class="btn-white">Request Demo</span>
    </div>
  </div>
</header>

<nav class="nav">
  <div class="wrap">
    <div class="brand"><span class="dot"></span>Vetrasol</div>
    <div class="menu">
      <span class="on">Home</span><span>Integration</span><span>Lead Capture</span><span>Feature</span><span>Contact Us</span>
    </div>
  </div>
</nav>

<section class="hero">
  <div class="art" role="img" aria-label="Hand holding floating blue cubes with business icons over a digital chart backdrop"></div>
  <h1><span>Lorem Ipsum</span> is<br>dummy text</h1>
  <p>Contrary to popular belief, Lorem Ipsum is not simply random text. It has roots in a piece of classical Latin literature from 45 BC, making it over 2000 years old.</p>
  <span class="btn-sky">Request a demo</span>
</section>

<section class="intro">
  <h2>Lorem Ipsum is simply dummy text</h2>
  <p>There are many variations of passages of Lorem Ipsum available, but the majority have suffered alteration in some form, by injected humour, or randomised words which don't look even slightly believable. If you are going to use a passage of Lorem Ipsum, you need to be sure there isn't anything embarrassing hidden in the middle of text. All the Lorem Ipsum generators on the Internet tend to repeat predefined chunks as necessary, making</p>
</section>

<section class="section features">
  <h2>Lorem Ipsum</h2>
  <p class="lead">Contrary to popular belief, Lorem Ipsum is not simply random text.</p>
  <div class="cards">
    <div class="feature"><div class="icon" role="img" aria-label="Target with arrow illustration" style="background:#f26b57"></div><h3>Lorem Ipsum</h3><p>There are many variations of passages of Lorem Ipsum available, but the majority have suffered</p></div>
    <div class="feature"><div class="icon" role="img" aria-label="Multi-tool with ruler and brush illustration" style="background:#f0a34a"></div><h3>Lorem Ipsum</h3><p>There are many variations of passages of Lorem Ipsum available, but the majority have suffered</p></div>
    <div class="feature"><div class="icon" role="img" aria-label="Thinking person with cloud and gear illustration" style="background:#f7c24a"></div><h3>Lorem Ipsum</h3><p>There are many variations of passages of Lorem Ipsum available, but the majority have suffered</p></div>
    <div class="feature"><div class="icon" role="img" aria-label="Hummingbird illustration" style="background:#8b6aa8"></div><h3>Lorem Ipsum</h3><p>There are many variations of passages of Lorem Ipsum available, but the majority have suffered</p></div>
  </div>
</section>

<section class="cta" role="img" aria-label="Dimmed photo of colleagues talking at a desk">
  <h2>Lorem Ipsum is simply dummy text.</h2>
  <p>Contrary to popular belief, Lorem Ipsum is not simply random text. It has roots in a piece of classical Latin literature from 45 BC, making it over 2000 years old.</p>
  <span class="btn-sky">Request a demo</span>
</section>

<section class="section gallery">
  <h2>Lorem Ipsum</h2>
  <p class="lead">Contrary to popular belief, Lorem Ipsum is not simply random text.</p>
  <div class="cards">
    <div class="tile" role="img" aria-label="Photo of a smiling woman at work" style="background:linear-gradient(160deg,#8a7a6a,#3d3630)">
      <div class="over"><h3>Lorem Ipsum</h3><p>It is a long established fact that a reader will be distracted by the readable con</p><div class="more">+ Read More</div></div>
    </div>
    <div class="tile" role="img" aria-label="Photo of two shoppers with bags" style="background:linear-gradient(160deg,#c9c2bb,#5a5556)"><div class="cap">Lorem Ipsum</div><div class="plus">+</div></div>
    <div class="tile" role="img" aria-label="Photo of a sales rep with a clipboard talking to a client" style="background:linear-gradient(160deg,#e2e4e6,#8b8e93)"><div class="cap">Lorem Ipsum</div><div class="plus">+</div></div>
    <div class="tile" role="img" aria-label="Photo of a businessman in a busy office" style="background:linear-gradient(160deg,#c8c6c2,#4a4f57)"><div class="cap">Lorem Ipsum</div><div class="plus">+</div></div>
  </div>
</section>

<section class="cta" role="img" aria-label="Dimmed photo of a smiling woman in a shop">
  <h2>Lorem Ipsum is simply dummy text.</h2>
  <p>Contrary to popular belief, Lorem Ipsum is not simply random text. It has roots in a piece of classical Latin literature from 45 BC, making it over 2000 years old.</p>
  <span class="btn-sky">Learn More</span>
</section>

<section class="section offers">
  <h2>Lorem Ipsum</h2>
  <p class="lead">Contrary to popular belief, Lorem Ipsum is not simply random text.</p>
  <div class="cards">
    <div class="offer" role="img" aria-label="Photo of a shopkeeper taking a card payment" style="background:linear-gradient(160deg,#6b5a4a,#2e2823)"><h3>Lorem Ipsum</h3><div class="more">+ Read More</div></div>
    <div class="offer" role="img" aria-label="Photo of a happy woman holding shopping bags" style="background:linear-gradient(160deg,#7a6d80,#3c4a52)"><h3>Lorem Ipsum</h3><div class="more">+ Read More</div></div>
    <div class="offer" role="img" aria-label="Photo of a red discount tag" style="background:linear-gradient(160deg,#c0403a,#7a6a4a)"><h3>Lorem Ipsum</h3><div class="more">+ Read More</div></div>
    <div class="offer" role="img" aria-label="Photo of a sale price tag" style="background:linear-gradient(160deg,#b85a55,#8a7a6a)"><h3>Lorem Ipsum</h3><div class="more">+ Read More</div></div>
  </div>
</section>

<footer class="footer">
  <div class="wrap">
    <div class="brand"><span class="dot"></span>Vetrasol</div>
    <div class="addr">
      <h4>ADDRESS</h4>
      <p>Lorem Ipsum is simply dummy text of the<br>printing and typesetting industry.</p>
      <p><b>Email:</b> info@example.com</p>
      <p><b>Phone:</b> 000-000-0000</p>
      <div class="social"><span></span><span></span><span></span><span></span></div>
    </div>
    <ul class="links">
      <h4>QUICK LINKS</h4>
      <li class="on">Home</li><li>Integration</li><li>Lead Capture</li><li>Feature</li><li>Contact Us</li><li>Login</li>
    </ul>
    <ul>
      <h4>SUPPORT</h4>
      <li>Help Center</li><li>Free Online Training</li><li>Developer Center</li>
    </ul>
  </div>
</footer>
<div class="copy">©2019 by Vetrasol. All rights reserved.</div>

</body>
</html>
```